We need a complete design for our construction company KELSO CONSTRUCTION based in Auckland New Zealand, we need a logo, website, business card, vehicle design etc..
We are a mid to high-end construction company who work mostly on residential projects and some commercial.

What we want to see in the design;
Professional,
Architectural,
Simple,
Alternative,

We want the design to communicate professionalism, high quality wormanship and and quality service.

Target Market(s)

People looking for a quality building/ construction company

Industry/Entity Type

Construction Company

Contact Information for Business Card

KELSO CONSTRUCTION.co.nz
Remi Tulvane
remi@kelsoconstruction-example.co.nz
021 5870 463

Logo Text

KELSO CONSTRUCTION

Number of Pages Required

5+ page

Font styles to use
Sans Serif

Colors

Designer to choose colors to be used in the design.

Requirements
Must have
• Must appear high end, professional, quality, be simple, easy to use, give security to potential clients
Nice to have
• high-quality photos of our recent projects
• about us page
• blog page
• contact us page
• high quality content
Should not have
• should not be hard to use and have too much going on.

```html
<!DOCTYPE html>
<html lang="en">
<head>
<meta charset="utf-8">
<title>Kelso Construction</title>
<link href="https://fonts.googleapis.com/css2?family=Open+Sans:wght@400;600;700;800&family=Merriweather:ital,wght@0,400;0,700;1,400&display=swap" rel="stylesheet">
<style>
:root{
  --ink:#1d1d1f;
  --dark:#262626;
  --yellow:#f4d314;
  --navy:#1e3563;
  --grey:#6a6a6a;
  --light:#f6f6f6;
  --white:#ffffff;
  --sans:'Open Sans',Arial,sans-serif;
  --serif:'Merriweather',Georgia,serif;
}
*{box-sizing:border-box;margin:0;padding:0}
html,body{width:1200px;height:3673px;overflow:hidden}
body{font-family:var(--serif);color:var(--grey);background:var(--white);position:relative}
section,header,footer{position:absolute;left:0;width:1200px}
.abs{position:absolute}

/* header / hero */
.hero{top:0;height:563px;background:linear-gradient(180deg,#141414 0%,#2a2c30 45%,#3a3d42 75%,#1d1e21 100%)}
.hero-photo{position:absolute;inset:0;background:linear-gradient(90deg,rgba(20,20,20,.75),rgba(20,20,20,.2) 60%,rgba(20,20,20,.5)),linear-gradient(0deg,#4a4d52 0%,#2b2d31 40%,transparent 70%)}
.brand{left:142px;top:16px;display:flex;align-items:center;gap:10px;color:var(--yellow);font-family:var(--sans);font-weight:700;font-size:15px;letter-spacing:3px;white-space:nowrap}
.brand-mark{width:38px;height:38px;border:2px solid var(--yellow);flex:none}
.topbar{left:500px;top:12px;width:560px;font-family:var(--sans);font-size:10px;color:#ddd;white-space:nowrap}
.topbar .item{position:absolute;top:0}
.topbar .welcome{right:0}
.topbar .welcome b{color:var(--yellow);font-weight:600}
.nav{left:500px;top:44px;display:flex;gap:22px;font-family:var(--sans);font-size:11px;font-weight:700;color:#fff;letter-spacing:.4px;white-space:nowrap}
.nav .active{border-bottom:2px solid var(--yellow);padding-bottom:10px}
.search{left:1046px;top:44px}
.hero-copy{left:235px;top:170px;width:860px;color:#eee}
.hero-copy h1{font-family:var(--sans);font-weight:800;font-size:37px;color:#fff;margin-bottom:22px}
.hero-copy h1 span{color:var(--yellow)}
.hero-copy p{font-size:13px;line-height:22px;margin-bottom:18px}
.btn{display:inline-block;background:var(--yellow);color:var(--ink);font-family:var(--sans);font-weight:700;font-size:13px;padding:10px 42px;border-radius:3px;margin-top:6px}
.dots{left:1024px;top:514px;display:flex;gap:12px}
.dots i{width:8px;height:8px;border-radius:50%;background:#fff;display:block}
.dots i.on{background:var(--yellow)}
.scroll-down{left:577px;top:540px;width:46px;height:46px;border-radius:50%;background:var(--yellow);border:3px solid #fff;z-index:2;display:flex;align-items:center;justify-content:center}

/* section titles */
.sec-title{position:absolute;left:0;width:1200px;display:flex;align-items:center;justify-content:center;gap:26px;font-family:var(--serif);font-size:15px;color:#444}
.sec-title::before,.sec-title::after{content:"";width:230px;height:2px;background:linear-gradient(90deg,var(--yellow),var(--navy))}
.sec-title::after{background:linear-gradient(90deg,var(--navy),var(--yellow))}

/* about */
.about{top:563px;height:441px;background:var(--white)}
.about-text{left:154px;top:100px;width:478px;font-size:10px;line-height:15px}
.about-text p{margin-bottom:11px}
.about-photo{left:671px;top:110px;width:377px;height:302px;border-radius:4px;background:linear-gradient(135deg,#e9e3dd 0%,#c98a56 35%,#7d4a28 55%,#d9b08a 75%,#efe9e2 100%)}

/* why */
.why{top:1004px;height:458px;background:var(--light)}
.why-line{left:330px;top:157px;width:540px;border-top:2px dashed #bbb}
.feature{position:absolute;top:110px;width:300px;text-align:center}
.feature .icon{width:88px;height:88px;border-radius:50%;background:var(--navy);margin:0 auto 26px;display:flex;align-items:center;justify-content:center}
.feature h3{font-family:var(--serif);font-size:15px;color:var(--ink);font-weight:700;margin-bottom:20px}
.feature p{font-size:10.5px;line-height:16px;margin-bottom:14px;padding:0 12px}

/* services */
.services{top:1462px;height:448px;display:flex}
.service{position:relative;width:600px;height:448px;padding:37px 46px 0 154px;overflow:hidden}
.service.res{background:linear-gradient(135deg,#e4c20c,var(--yellow) 40%,#f5d83a)}
.service.com{background:linear-gradient(135deg,#182c54,var(--navy) 50%,#2a4577);padding-left:46px;padding-right:110px}
.service h2{font-family:var(--serif);font-weight:400;font-size:21px;margin-bottom:28px}
.service.res h2{color:var(--navy)}
.service.com h2{color:var(--yellow)}
.service p{font-size:12px;line-height:16px}
.service.res p{color:var(--ink)}
.service.com p{color:var(--yellow)}
.service p em{font-style:italic}

/* projects */
.projects{top:1910px;height:901px;background:var(--white)}
.projects-intro{left:150px;top:108px;width:900px;text-align:center;font-size:15px;line-height:27px;color:#555}
.tabs{left:429px;top:196px;display:flex;font-size:15px;font-family:var(--serif)}
.tabs span{width:196px;height:47px;display:flex;align-items:center;justify-content:center;color:var(--ink)}
.tabs .on{background:var(--yellow)}
.tabs .off{background:var(--navy);color:#fff;width:215px;height:42px;margin-top:5px}
.tile{position:absolute;overflow:hidden}
.tile .label{position:absolute;left:0;right:0;bottom:0;height:72px;background:rgba(30,53,99,.85);color:#fff;font-family:var(--serif);font-size:21px;letter-spacing:2px;display:flex;align-items:center;justify-content:center}
.tile-feature{background:linear-gradient(160deg,#b39a2c,#7d6d2a)}
.tile-feature .overlay{position:absolute;inset:0;background:rgba(30,53,99,.55);padding:28px 20px;text-align:center;color:#fff}
.tile-feature h4{font-family:var(--serif);font-weight:400;font-size:21px;letter-spacing:2px;color:var(--yellow);margin-bottom:14px}
.tile-feature p{font-style:italic;font-size:12px;line-height:24px}
.arrows{display:flex;gap:12px}
.arrows i{width:34px;height:34px;display:flex;align-items:center;justify-content:center}
.arrows.solid i{background:var(--navy)}
.arrows.outline i{background:#fff;border:1px solid #ccc}

/* testimonials */
.testimonials{top:2811px;height:483px;background:linear-gradient(90deg,var(--navy) 0%,#2b3f63 30%,#8a8a3a 65%,var(--yellow) 100%)}
.testimonials .sec-title{color:#fff}
.testimonials .sec-title::before,.testimonials .sec-title::after{background:#fff;height:1px}
.quote-card{position:absolute;top:111px;width:450px;height:230px;background:#fff;box-shadow:0 4px 14px rgba(0,0,0,.25);padding:82px 46px 0;text-align:center}
.avatar{position:absolute;left:188px;top:20px;width:74px;height:74px;border-radius:50%;background:linear-gradient(180deg,#9a9a9a,#4a4a4a);border:3px solid #fff;box-shadow:0 1px 4px rgba(0,0,0,.3)}
.quote-card p{font-size:11px;line-height:17px;margin-top:12px}
.quote-card p b{color:var(--navy)}
.quote-card h5{font-family:var(--serif);font-style:italic;font-weight:400;font-size:17px;color:var(--navy);margin-top:8px}
.quote-card small{font-size:8px;color:#888}
.qmark{position:absolute;font-family:var(--serif);font-size:54px;font-weight:700;color:var(--navy);line-height:1}

/* footer */
.footer{top:3294px;height:379px;background:var(--dark);color:#ddd}
.footer h6{font-family:var(--serif);font-weight:400;font-size:15px;color:#fff;position:absolute;top:42px}
.footer .brand{position:absolute;left:152px;top:95px;font-size:11px;letter-spacing:2px}
.footer .brand .brand-mark{width:28px;height:28px}
.office{position:absolute;left:152px;width:220px;font-size:10px;line-height:14px;color:#eee}
.office b{display:block;font-size:11px;margin-bottom:3px}
.map{left:399px;top:74px;width:336px;height:232px;background:linear-gradient(135deg,#e7e7e2,#d7dbd0 40%,#eadfb8 60%,#e3e3de);border:4px solid #fff}
.newsletter{position:absolute;left:811px;top:86px;width:260px;font-size:12px;line-height:19px;color:#eee}
.field{position:absolute;left:811px;top:152px;width:236px;height:38px;background:#fff;border-radius:19px;display:flex;align-items:center;padding-left:16px;font-size:11px;color:#999}
.field span{position:absolute;right:0;top:0;height:38px;width:78px;border-radius:19px;background:var(--yellow);color:var(--ink);font-weight:700;display:flex;align-items:center;justify-content:center;font-size:12px}
.follow{position:absolute;left:811px;top:230px;display:flex;align-items:center;gap:14px;font-size:14px;color:#fff}
.follow i{width:20px;height:20px;border-radius:50%;background:#fff;display:block}
.copyright{position:absolute;left:0;top:344px;width:1200px;border-top:1px solid #444;padding-top:10px;text-align:center;font-size:9px;color:#bbb}
</style>
</head>
<body>

<header class="hero">
  <div class="hero-photo" role="img" aria-label="City skyline with high-rise buildings at dusk"></div>
  <div class="abs brand"><span class="brand-mark"></span>KELSO CONSTRUCTION</div>
  <div class="abs topbar">
    <span class="item" style="left:0">&#9742; (+64) 9 555 0147</span>
    <span class="item" style="left:118px">&#9993; hello@kelsoconstruction-example.co.nz</span>
    <span class="item welcome">Welcome visitor! you can <b>Log in</b> or <b>Sign Up</b></span>
  </div>
  <nav class="abs nav">
    <span class="active">HOME</span><span>ABOUT</span><span>SERVICES</span><span>PORTFOLIO</span><span>BLOG</span><span>TESTIMONIAL</span><span>CONTACT</span>
  </nav>
  <svg class="abs search" width="14" height="14" viewBox="0 0 14 14"><circle cx="6" cy="6" r="4.5" fill="none" stroke="#f4d314" stroke-width="1.6"/><line x1="9.5" y1="9.5" x2="13" y2="13" stroke="#f4d314" stroke-width="1.6"/></svg>
  <div class="abs hero-copy">
    <h1>Welcome to <span>Kelso Construction.</span></h1>
    <p>Lorem ipsum dolor sit amet, consectetur adipiscing elit, sed do eiusmod tempor incididunt ut labore et dolore magna aliqua. Cursus eget nunc scelerisque viverra mauris in. In arcu cursus euismod quis viverra nibh. Varius duis at consectetur lorem.</p>
    <p>Pellentesque habitant morbi tristique senectus et netus et malesuada fames. Volutpat consequat mauris nunc congue nisi vitae.</p>
    <span class="btn">Learn More &gt;&gt;&gt;</span>
  </div>
  <div class="abs dots"><i></i><i></i><i class="on"></i><i></i><i></i><i></i><i></i></div>
</header>

<div class="abs scroll-down"><svg width="18" height="12" viewBox="0 0 18 12"><polyline points="2,2 9,9 16,2" fill="none" stroke="#1d1d1f" stroke-width="2.5"/></svg></div>

<section class="about">
  <div class="sec-title" style="top:30px">ABOUT US</div>
  <div class="abs about-text">
    <p>Lorem ipsum dolor sit amet, consectetur adipiscing elit, sed do eiusmod tempor incididunt ut labore et dolore magna aliqua. Cursus eget nunc scelerisque viverra mauris in. In arcu cursus euismod quis viverra nibh. Varius duis at consectetur lorem. Pellentesque habitant morbi tristique senectus et netus et malesuada fames. Volutpat consequat mauris nunc congue nisi vitae. Eu scelerisque felis imperdiet proin fermentum leo vel orci porta. Nibh tellus molestie nunc non blandit massa enim nec dui. Tempor id eu nisl nunc mi ipsum faucibus vitae aliquet.</p>
    <p>Tristique senectus et netus et malesuada. Eu scelerisque felis imperdiet proin fermentum leo vel orci. Scelerisque felis imperdiet proin fermentum leo. Quisque sagittis purus sit amet volutpat consequat.</p>
    <p>Viverra aliquet eget sit amet tellus cras adipiscing. Cursus mattis molestie a iaculis at. Auctor urna nunc id cursus metus aliquam eleifend mi. Nulla at volutpat diam ut venenatis tellus. Cursus risus at ultrices mi. Eget est lorem ipsum dolor sit. Sed vulputate mi sit amet mauris.</p>
    <p>Id porta nibh venenatis cras sed felis eget velit aliquet. Nulla facilisi cras fermentum odio eu feugiat pretium nibh. Volutpat sed cras ornare arcu.</p>
  </div>
  <div class="abs about-photo" role="img" aria-label="Curved timber staircase seen from above with a worker"></div>
</section>

<section class="why">
  <div class="sec-title" style="top:40px">Why Choose Us</div>
  <div class="abs why-line"></div>
  <div class="feature" style="left:137px">
    <div class="icon"><svg width="44" height="44" viewBox="0 0 44 44"><path d="M8 24 Q22 8 36 24 Z" fill="#f4d314"/><rect x="6" y="24" width="32" height="4" rx="2" fill="#f4d314"/><rect x="12" y="30" width="20" height="8" fill="#c9a15c"/></svg></div>
    <h3>consectetur adipiscing elit</h3>
    <p>Volutpat consequat mauris nunc congue nisi vitae. Eu scelerisque felis imperdiet proin fermentum leo vel orci porta. Nibh tellus molestie nunc non blandit massa enim nec dui. Tempor id eu nisl nunc mi ipsum faucibus vitae aliquet. Vitae proin sagittis nisl rhoncus.</p>
    <p>Nec sagittis aliquam malesuada bibendum arcu vitae elementum curabitur vitae. Porttitor rhoncus dolor purus non enim praesent elementum.</p>
  </div>
  <div class="feature" style="left:450px">
    <div class="icon"><svg width="44" height="44" viewBox="0 0 44 44"><line x1="10" y1="10" x2="34" y2="34" stroke="#f4d314" stroke-width="5" stroke-linecap="round"/><line x1="34" y1="10" x2="10" y2="34" stroke="#fff" stroke-width="4" stroke-linecap="round"/></svg></div>
    <h3>consectetur adipiscing elit</h3>
    <p>Volutpat consequat mauris nunc congue nisi vitae. Eu scelerisque felis imperdiet proin fermentum leo vel orci porta. Nibh tellus molestie nunc non blandit massa enim nec dui. Tempor id eu nisl nunc mi ipsum faucibus vitae aliquet. Vitae proin sagittis nisl rhoncus.</p>
    <p>Nec sagittis aliquam malesuada bibendum arcu vitae elementum curabitur vitae. Porttitor rhoncus dolor purus non enim praesent elementum.</p>
  </div>
  <div class="feature" style="left:763px">
    <div class="icon"><svg width="44" height="44" viewBox="0 0 44 44"><rect x="6" y="12" width="32" height="12" fill="#f4d314"/><line x1="22" y1="24" x2="22" y2="36" stroke="#fff" stroke-width="4"/></svg></div>
    <h3>consectetur adipiscing elit</h3>
    <p>Volutpat consequat mauris nunc congue nisi vitae. Eu scelerisque felis imperdiet proin fermentum leo vel orci porta. Nibh tellus molestie nunc non blandit massa enim nec dui. Tempor id eu nisl nunc mi ipsum faucibus vitae aliquet. Vitae proin sagittis nisl rhoncus.</p>
    <p>Nec sagittis aliquam malesuada bibendum arcu vitae elementum curabitur vitae. Porttitor rhoncus dolor purus non enim praesent elementum.</p>
  </div>
</section>

<section class="services">
  <div class="service res" role="img" aria-label="Residential services over a faint building photo">
    <h2>Residential Services</h2>
    <p>Lorem ipsum dolor sit amet, consectetur adipiscing elit, sed do eiusmod tempor incididunt ut labore et dolore magna aliqua. Cursus eget nunc scelerisque viverra mauris in.<br>
    <em>What is Lorem Ipsum?</em><br>
    Lorem Ipsum is simply dummy text of the printing and typesetting industry. Lorem Ipsum has been the industry's standard dummy text ever since the 1500s, when an unknown printer took a galley of type and scrambled it to make a type specimen book.<br>
    <em>Why do we use it?</em><br>
    It is a long established fact that a reader will be distracted by the readable content of a page when looking at its layout. The point of using Lorem Ipsum is that it has a more-or-less normal distribution of letters, making it look like readable English.<br>
    <em>Where can we get some?</em><br>
    There are many variations of passages of Lorem Ipsum available, but the majority have suffered alteration in some form, by injected humour, or randomised words.</p>
  </div>
  <div class="service com" role="img" aria-label="Commercial services over a faint glass tower photo">
    <h2>Commercial Services</h2>
    <p>Lorem ipsum dolor sit amet, consectetur adipiscing elit, sed do eiusmod tempor incididunt ut labore et dolore magna aliqua. Cursus eget nunc scelerisque viverra mauris in.<br>
    <em>What is Lorem Ipsum?</em><br>
    Lorem Ipsum is simply dummy text of the printing and typesetting industry. Lorem Ipsum has been the industry's standard dummy text ever since the 1500s, when an unknown printer took a galley of type and scrambled it to make a type specimen book.<br>
    <em>Why do we use it?</em><br>
    It is a long established fact that a reader will be distracted by the readable content of a page when looking at its layout. The point of using Lorem Ipsum is that it has a more-or-less normal distribution of letters, making it look like readable English.<br>
    <em>Where can we get some?</em><br>
    There are many variations of passages of Lorem Ipsum available, but the majority have suffered alteration in some form, by injected humour, or randomised words.</p>
  </div>
</section>

<section class="projects">
  <div class="sec-title" style="top:36px">Our Projects</div>
  <p class="abs projects-intro">Lorem ipsum dolor sit amet, consectetur adipiscing elit, sed do eiusmod tempor incididunt ut labore et dolore magna aliqua. Cursus eget nunc scelerisque viverra mauris in. In arcu cursus euismod quis viverra nibh.</p>
  <div class="abs tabs"><span class="on">Residential</span><span class="off">Commercial</span></div>

  <div class="tile tile-feature" style="left:113px;top:282px;width:262px;height:262px" role="img" aria-label="Modern residence exterior">
    <div class="overlay">
      <h4>ASHBY VILLA</h4>
      <p>Lorem ipsum dolor sit amet, consectetur adipiscing elit, sed do eiusmod tempor incididunt ut labore et dolore magna aliqua. Cursus eget nunc scelerisque viverra mauris in.</p>
    </div>
  </div>
  <div class="tile" style="left:392px;top:282px;width:448px;height:262px;background:linear-gradient(150deg,#2f4a78,#6f8fb8 45%,#c9d6e4 70%,#8ea2ba)" role="img" aria-label="Curved metal facade of a contemporary building">
    <div class="label">HARBOUR HOUSE</div>
  </div>
  <div class="tile" style="left:855px;top:282px;width:233px;height:502px;background:linear-gradient(180deg,#dfe6ea,#b8c7d0 40%,#e9ecee 70%,#9aa8b1)" role="img" aria-label="White tiered apartment tower against a sky">
    <div class="label">COMMERCIAL</div>
  </div>
  <div class="tile" style="left:113px;top:559px;width:377px;height:225px;background:linear-gradient(90deg,#2b2b2b,#8a8a8a 50%,#2b2b2b)" role="img" aria-label="Long curved tunnel corridor">
    <div class="label">TUNNEL</div>
  </div>
  <div class="tile" style="left:502px;top:559px;width:338px;height:225px;background:linear-gradient(160deg,#3a3f44,#9aa3aa 50%,#4b5257)" role="img" aria-label="Interior of a science laboratory building">
    <div class="label">SCIENCE LAB</div>
  </div>

  <div class="abs arrows solid" style="left:557px;top:811px">
    <i><svg width="10" height="14" viewBox="0 0 10 14"><polyline points="8,1 2,7 8,13" fill="none" stroke="#fff" stroke-width="2"/></svg></i>
    <i><svg width="10" height="14" viewBox="0 0 10 14"><polyline points="2,1 8,7 2,13" fill="none" stroke="#fff" stroke-width="2"/></svg></i>
  </div>
</section>

<section class="testimonials">
  <div class="sec-title" style="top:32px">Testimonials</div>
  <div class="quote-card" style="left:113px">
    <div class="avatar" role="img" aria-label="Client portrait"></div>
    <span class="qmark" style="left:24px;top:64px">&ldquo;</span>
    <span class="qmark" style="right:24px;bottom:2px">&rdquo;</span>
    <p>Lorem ipsum dolor sit amet, consectetur adipiscing elit, sed do eiusmod tempor incididunt ut labore et dolore magna aliqua. Cursus eget nunc scelerisque viverra mauris in. In arcu cursus euismod quis viverra nibh. <b>Read More &gt;&gt;&gt;</b></p>
    <h5>Owen Harlow</h5>
    <small>Customer ID #1</small>
  </div>
  <div class="quote-card" style="left:637px">
    <div class="avatar" role="img" aria-label="Client portrait"></div>
    <span class="qmark" style="left:24px;top:64px">&ldquo;</span>
    <span class="qmark" style="right:24px;bottom:2px">&rdquo;</span>
    <p>Lorem ipsum dolor sit amet, consectetur adipiscing elit, sed do eiusmod tempor incididunt ut labore et dolore magna aliqua. Cursus eget nunc scelerisque viverra mauris in. In arcu cursus euismod quis viverra nibh. <b>Read More &gt;&gt;&gt;</b></p>
    <h5>Owen Harlow</h5>
    <small>Customer ID #2</small>
  </div>
  <div class="abs arrows outline" style="left:557px;top:414px">
    <i><svg width="10" height="14" viewBox="0 0 10 14"><polyline points="8,1 2,7 8,13" fill="none" stroke="#333" stroke-width="2"/></svg></i>
    <i><svg width="10" height="14" viewBox="0 0 10 14"><polyline points="2,1 8,7 2,13" fill="none" stroke="#333" stroke-width="2"/></svg></i>
  </div>
</section>

<footer class="footer">
  <h6 style="left:152px">About</h6>
  <div class="brand"><span class="brand-mark"></span>KELSO CONSTRUCTION</div>
  <div class="office" style="top:150px"><b>Office Address #1</b>Your Office address #0123<br>Your City address #0123<br>M : (+64) 9 555 0147<br>E : office@kelsoconstruction-example.co.nz</div>
  <div class="office" style="top:238px"><b>Office Address #2</b>Your Office address #0123<br>Your City address #0123<br>M : (+64) 9 555 0147<br>E : office@kelsoconstruction-example.co.nz</div>

  <h6 style="left:399px">Location Map</h6>
  <div class="abs map" role="img" aria-label="Street map showing the office location"></div>

  <h6 style="left:811px">Newsletter</h6>
  <p class="newsletter">Register for your email address to learn about us.</p>
  <div class="field">e.g. you@mail.com<span>Submit</span></div>
  <div class="follow">Follow us : <i></i><i></i><i></i><i></i></div>

  <div class="copyright">&copy; 2018 Kelso Construction &nbsp;-&nbsp; All Rights Reserved.</div>
</footer>

</body>
</html>
```